Portrait of a Learner Infographic

A portrait of a learner is an aspirational idea of the skills a student should have at graduation. "Learner" recognizes that learning continues after graduation.
An info graphic is needed to convey the skills that have been identified. A full version is needed that can be posted on classroom walls (11x17) and a simplified version to share on the website and any other means identified.
The Birchfield School District is in Concord, New Hampshire, the capital city for NH. The district serves 4,100 diverse students in seven schools and a regional career and technical education center.
The district's hex colors are Green: #007137 and Blue: #085bab
Each school has its own unique colors.
The design should be positive, aspirational and still professional.
Teachers, students and parents
Public school district

```html
<!DOCTYPE html>
<html lang="en">
<head>
<meta charset="utf-8">
<title>Birchfield School District – Portrait of a Learner</title>
<link rel="stylesheet" href="https://fonts.googleapis.com/css2?family=Poppins:wght@400;500;600;700;800&display=swap">
<style>
  :root {
    --green: #007137;
    --green-box: #0b7a3c;
    --green-dark: #053f1f;
    --blue: #085bab;
    --blue-band: #0455c0;
    --navy: #1a2a6c;
    --ink: #111111;
    --body: #222222;
    --col-blue: #eef3fb;
    --col-green: #e6f3ec;
    --stage: #dfe3e8;
    --paper: #ffffff;
    --ring: rgba(110, 180, 145, 0.6);
  }
  * { box-sizing: border-box; margin: 0; padding: 0; }
  html, body { width: 921px; height: 1200px; overflow: hidden; background: var(--stage); }
  body { position: relative; font-family: 'Poppins', sans-serif; color: var(--ink); }

  .poster {
    position: absolute; left: 81px; top: 13px;
    width: 1116px; height: 1725px;
    background: var(--paper);
    transform: scale(0.68); transform-origin: top left;
    overflow: hidden;
  }
  .abs { position: absolute; }

  .district-name {
    left: 63px; top: 118px; width: 360px;
    font-weight: 700; font-size: 38px; line-height: 44px;
    color: var(--green);
  }
  .eyebrow {
    left: 435px; top: 75px;
    font-weight: 500; font-size: 28px; line-height: 32px; letter-spacing: 5px;
    color: var(--ink); white-space: nowrap;
  }
  .headline {
    left: 432px; top: 112px;
    font-weight: 800; font-size: 80px; line-height: 65px; letter-spacing: -1px;
    color: var(--green); white-space: nowrap;
  }
  .intro {
    left: 63px; top: 272px; z-index: 3;
    font-weight: 500; font-size: 22px; line-height: 27px;
    color: var(--ink); white-space: nowrap;
  }

  .trait-box { color: #fff; background: var(--green-box); overflow: hidden; z-index: 2; }
  .trait-box h2 { background: var(--green-dark); color: #fff; font-weight: 700; font-size: 28px; line-height: 30px; }
  .trait-box ul { list-style: none; }
  .trait-box li { position: relative; font-size: 18.5px; line-height: 20px; font-weight: 500; }
  .trait-box li.bullet::before {
    content: ""; position: absolute; left: -22px; top: 5px; width: 11px; height: 11px;
    border-radius: 50%; background: var(--green-dark);
  }

  .box-collab { left: 733px; top: 278px; width: 330px; height: 272px; border-radius: 50px 18px 18px 50px; }
  .box-collab h2 { height: 80px; padding: 26px 0 0 50px; }
  .box-collab ul { padding: 16px 0 0 140px; }
  .box-collab li { margin-bottom: 13px; }

  .box-self { left: 766px; top: 583px; width: 299px; height: 247px; border-radius: 30px 18px 60px 18px; }
  .box-self h2 { height: 62px; padding: 16px 0 0 70px; }
  .box-self ul { padding: 12px 0 0 107px; }
  .box-self li { margin-bottom: 9.5px; }

  .box-creative { left: 51px; top: 536px; width: 327px; height: 272px; border-radius: 18px 40px 80px 18px; }
  .box-creative h2 { height: 82px; padding: 18px 0 0 23px; }
  .box-creative ul { padding: 10px 0 0 53px; }
  .box-creative li { margin-bottom: 2.5px; }

  .portrait-ring {
    left: 289px; top: 304px; width: 538px; height: 538px; border-radius: 50%;
    border: 16px solid var(--ring); z-index: 1;
  }
  .portrait-photo {
    left: 308px; top: 323px; width: 500px; height: 500px; border-radius: 50%; z-index: 1;
    background: radial-gradient(circle at 50% 58%, #4a4a4a 0 32%, #1b5fd0 33%, #0a52c4 100%);
  }

  .scene { background: linear-gradient(180deg, #f4f6fa, #e3eaf6); border-radius: 6px; }
  .scene-team { left: 56px; top: 848px; width: 292px; height: 205px; }
  .scene-class { left: 411px; top: 840px; width: 257px; height: 213px; }
  .scene-study { left: 728px; top: 848px; width: 310px; height: 205px; }

  .band-black { left: 0; top: 1353px; width: 1116px; height: 140px; background: #000; }
  .band-blue { left: 0; top: 1493px; width: 1116px; height: 232px; background: var(--blue-band); }

  .skill-col { top: 1093px; height: 567px; }
  .col-collab { left: 66px; width: 304px; background: var(--col-blue); }
  .col-self { left: 388px; width: 304px; background: var(--col-green); }
  .col-creative { left: 710px; width: 344px; background: var(--col-blue); }

  .col-label {
    top: 1071px; height: 44px; z-index: 2;
    color: #fff; font-weight: 700; font-size: 24px; line-height: 44px;
    text-align: center; white-space: nowrap;
  }
  .label-collab { left: 107px; width: 220px; background: var(--green); }
  .label-self { left: 430px; width: 220px; background: var(--blue); }
  .label-creative { left: 747px; width: 276px; background: var(--green); }

  .skill { font-size: 15.8px; line-height: 18.5px; color: var(--body); font-weight: 400; }
  .skill svg { position: absolute; left: -46px; top: 2px; width: 26px; height: 26px; }
  .col-collab .skill { left: 70px; width: 195px; }
  .col-self .skill { left: 71px; width: 200px; }
  .col-creative .skill { left: 69px; width: 282px; font-size: 15.4px; line-height: 18px; }
</style>
</head>
<body>
<main class="poster">
  <div class="abs district-name">Birchfield<br>School District</div>
  <p class="abs eyebrow">BIRCHFIELD SCHOOL DISTRICT</p>
  <h1 class="abs headline">PORTRAIT OF A<br>LEARNER</h1>

  <p class="abs intro">Birchfield School District learners<br>are informed, compassionate<br>and capable citizens who<br>effectively, courageously<br>and responsibly direct<br>their lives and<br>positively impact<br>communities.</p>

  <div class="abs portrait-ring"></div>
  <div class="abs portrait-photo" role="img" aria-label="Photo of a smiling graduate in cap and gown holding a diploma, on a blue circle"></div>

  <section class="abs trait-box box-collab">
    <h2>COLLABORATIVE</h2>
    <ul>
      <li class="bullet">Emotional<br>intelligence</li>
      <li class="bullet">Civic minded</li>
      <li class="bullet">Compassionate<br>leader</li>
    </ul>
  </section>

  <section class="abs trait-box box-self">
    <h2>SELF-DIRECTED</h2>
    <ul>
      <li class="bullet">Responsible</li>
      <li class="bullet">Problem solver</li>
      <li class="bullet">Self-starter</li>
      <li class="bullet">Resilient</li>
      <li class="bullet">Growth mindset</li>
    </ul>
  </section>

  <section class="abs trait-box box-creative">
    <h2>CREATIVE &amp;<br>SKILLFUL</h2>
    <ul>
      <li>Critical &amp; analytical<br>thinker</li>
      <li class="bullet">Innovative</li>
      <li class="bullet">Informed risk-taker</li>
      <li class="bullet">Adaptable</li>
      <li class="bullet">Curious</li>
      <li class="bullet">Self-motivated</li>
    </ul>
  </section>

  <div class="abs scene scene-team" role="img" aria-label="Illustration of a team fitting puzzle pieces together"></div>
  <div class="abs scene scene-class" role="img" aria-label="Illustration of a presenter at a flip chart with seated students"></div>
  <div class="abs scene scene-study" role="img" aria-label="Illustration of students studying on stacked books with laptops"></div>

  <div class="abs band-black"></div>
  <div class="abs band-blue"></div>

  <section class="abs skill-col col-collab">
    <div class="abs skill" style="top:55px"><svg viewBox="0 0 26 26"><circle cx="7" cy="7" r="4" fill="#1a2a6c"/><circle cx="19" cy="7" r="4" fill="#1a2a6c"/><circle cx="13" cy="19" r="5" fill="#1a2a6c"/></svg>Respectfully engages with others</div>
    <div class="abs skill" style="top:115px"><svg viewBox="0 0 26 26"><rect x="3" y="3" width="20" height="20" rx="4" fill="#1a2a6c"/><circle cx="13" cy="13" r="5" fill="#fff"/></svg>Asks challenging and probing questions in a manner that preserves healthy relationships</div>
    <div class="abs skill" style="top:215px"><svg viewBox="0 0 26 26"><path d="M13 23 3 12a5 5 0 0 1 10-6 5 5 0 0 1 10 6Z" fill="#1a2a6c"/></svg>Speaks and acts inclusively to support equity, safety and belonging with actions and behaviors that support an environment where all feel safe to learn and engage</div>
    <div class="abs skill" style="top:420px"><svg viewBox="0 0 26 26"><rect x="4" y="12" width="6" height="11" fill="#1a2a6c"/><rect x="12" y="8" width="10" height="15" rx="2" fill="#1a2a6c"/><circle cx="7" cy="5" r="2" fill="#1a2a6c"/><circle cx="19" cy="3" r="2" fill="#1a2a6c"/></svg>Demonstrates and advocates for positive and sustainable change for oneself and others</div>
  </section>

  <section class="abs skill-col col-self">
    <div class="abs skill" style="top:48px"><svg viewBox="0 0 26 26"><circle cx="13" cy="12" r="10" fill="#1a2a6c"/><circle cx="13" cy="11" r="4" fill="#fff"/></svg>Understands own strengths, needs and interests</div>
    <div class="abs skill" style="top:130px"><svg viewBox="0 0 26 26"><rect x="4" y="12" width="4" height="11" fill="#1a2a6c"/><rect x="11" y="4" width="4" height="19" fill="#1a2a6c"/><rect x="18" y="9" width="4" height="14" fill="#1a2a6c"/></svg>Accesses credible resources &amp; seeks help to support growth &amp; create actionable plans</div>
    <div class="abs skill" style="top:230px"><svg viewBox="0 0 26 26"><rect x="3" y="4" width="18" height="17" rx="2" fill="#1a2a6c"/><circle cx="19" cy="19" r="5" fill="#fff" stroke="#1a2a6c" stroke-width="2"/></svg>Uses effective time management, planning and communication to accomplish long and short term goals</div>
    <div class="abs skill" style="top:348px"><svg viewBox="0 0 26 26"><circle cx="13" cy="15" r="7" fill="none" stroke="#1a2a6c" stroke-width="3"/><circle cx="13" cy="15" r="2.5" fill="#1a2a6c"/><path d="M13 2v4M3 6l3 3M23 6l-3 3" stroke="#1a2a6c" stroke-width="2"/></svg>Perseveres through challenges and seeking new experiences</div>
    <div class="abs skill" style="top:430px"><svg viewBox="0 0 26 26"><circle cx="13" cy="11" r="7" fill="#1a2a6c"/><rect x="10" y="18" width="6" height="5" fill="#1a2a6c"/></svg>Approaches problems as opportunities and generates solutions</div>
  </section>

  <section class="abs skill-col col-creative">
    <div class="abs skill" style="top:40px"><svg viewBox="0 0 26 26"><circle cx="6" cy="8" r="4" fill="#1a2a6c"/><circle cx="20" cy="8" r="4" fill="#1a2a6c"/><circle cx="13" cy="17" r="5" fill="#1a2a6c"/></svg>Accesses, evaluates, applies and communicates diverse forms of information for a variety of audiences and purposes</div>
    <div class="abs skill" style="top:130px"><svg viewBox="0 0 26 26"><path d="M4 10 13 4l9 6v12H4Z" fill="#1a2a6c"/><path d="M9 15l3 3 5-6" stroke="#fff" stroke-width="2" fill="none"/></svg>Makes productive and innovative decisions based on new learning that move an idea from concept to application</div>
    <div class="abs skill" style="top:220px"><svg viewBox="0 0 26 26"><path d="M3 11h5l12-7v18L8 15H3Z" fill="#1a2a6c"/></svg>Gains awareness of relevant technology and practices that enable production in a variety of fields</div>
    <div class="abs skill" style="top:310px"><svg viewBox="0 0 26 26"><circle cx="13" cy="13" r="8" fill="#1a2a6c"/><circle cx="13" cy="13" r="3" fill="#fff"/><circle cx="13" cy="3" r="2" fill="#1a2a6c"/><circle cx="13" cy="23" r="2" fill="#1a2a6c"/><circle cx="3" cy="13" r="2" fill="#1a2a6c"/><circle cx="23" cy="13" r="2" fill="#1a2a6c"/></svg>Learns processes that enable individuals and collaborative teams to plan, design, test, execute, evaluate, reflect and adapt</div>
    <div class="abs skill" style="top:400px"><svg viewBox="0 0 26 26"><circle cx="7" cy="8" r="4" fill="#1a2a6c"/><path d="M2 22l7-7 5 4 10-10" stroke="#1a2a6c" stroke-width="2.5" fill="none"/></svg>Uses evidence of successes and challenges to adapt practices or processes in a manner that supports future growth</div>
    <div class="abs skill" style="top:490px"><svg viewBox="0 0 26 26"><circle cx="13" cy="13" r="9" fill="#1a2a6c"/><path d="M13 5v16M7 10h12M7 16h12" stroke="#fff" stroke-width="1.5"/></svg>Applies content knowledge to form creative inferences or provide innovative solutions</div>
  </section>

  <h2 class="abs col-label label-collab">COLLABORATIVE</h2>
  <h2 class="abs col-label label-self">SELF-DIRECTED</h2>
  <h2 class="abs col-label label-creative">CREATIVE &amp; SKILLFUL</h2>
</main>
</body>
</html>
```